Velvet & Vine by Mona
Text 410.582.3174 to set up and appointment
Instagram is Velvet_VineByMona
Location 4182 Carrow Ln. Notthingham Md, 21094 Suit 204
Slogan "Polished Looks. Radiant Days.
Specializing in pressicion cuts, blonding, fades, perms, waxing and more

The salon is black, gun metal color mirror with led lights. Green plants and has natural wood countertops for accent colors. Modern yet elegant. I want the card simple but it needs something to really grab the clients attention. I like black, grey, gold, green, natural tones and hints of pink or gold coloring
I’m open to anything. I don’t have a logo. Suggestions are welcome

Target Market(s)

20-60 men and woman

Industry/Entity Type

Hairstylist / barber

The name of the show should be bold. Maybe the letters could raised I also like foil for shine added or a mat finish

Colors

Requirements
Must have
• I also like some floral Floral designs, but not too overpowering. I like Sparkle, Watercolor design, Or a geometric line in the background
Nice to have
• I’m really here because I need creative help. I’m open for suggestions. I’ll post a picture of the salon in inspiration if I can find it.
Should not have
• Checkered background

```html
<!DOCTYPE html>
<html lang="en">
<head>
<meta charset="utf-8">
<title>Velvet &amp; Vine by Mona — Business Card</title>
<link href="https://fonts.googleapis.com/css2?family=Outfit:wght@300;400;600;700&family=Mrs+Saint+Delafield&display=swap" rel="stylesheet">
<style>
  :root {
    --backdrop: #b6b6b6;
    --card-front: #e9d3a6;
    --card-front-glow: #f0dcb4;
    --card-back: #f3f3f3;
    --ink: #2f2f2f;
    --ink-soft: #3d3d3d;
    --gold: #c9a867;
    --gold-line: #b8955a;
  }
  * { margin: 0; padding: 0; box-sizing: border-box; }
  html, body {
    width: 1200px; height: 900px; overflow: hidden;
    background: var(--backdrop);
    font-family: "Outfit", sans-serif;
    color: var(--ink);
  }
  .card { position: absolute; overflow: hidden; }
  .card-front {
    left: 392px; top: 196px; width: 414px; height: 236px;
    background: radial-gradient(ellipse at 50% 40%, var(--card-front-glow) 0%, var(--card-front) 70%);
  }
  .card-back {
    left: 399px; top: 496px; width: 400px; height: 229px;
    background: var(--card-back);
  }
  .accent-lines { position: absolute; inset: 0; width: 100%; height: 100%; pointer-events: none; }

  /* front */
  .front-wordmark {
    position: absolute; left: 0; right: 0; top: 80px;
    text-align: center; font-weight: 700; color: var(--ink);
  }
  .front-wordmark .brand-main { display: block; font-size: 34px; line-height: 1.05; letter-spacing: 0.01em; }
  .front-wordmark .brand-sub { display: block; font-size: 10px; font-weight: 700; margin-top: 5px; }
  .front-tagline {
    position: absolute; left: 0; right: 0; top: 200px;
    text-align: center; font-size: 6px; letter-spacing: 0.32em;
    color: var(--ink-soft);
  }

  /* back */
  .services {
    position: absolute; left: 44px; top: 40px;
    border-left: 1px solid var(--ink); padding-left: 7px;
    font-size: 7.3px; line-height: 9.6px; font-weight: 300; color: var(--ink);
  }
  .script-slogan {
    position: absolute; left: 46px; top: 73px;
    font-family: "Mrs Saint Delafield", cursive;
    font-size: 15px; color: var(--ink-soft);
  }
  .holder { position: absolute; right: 42px; top: 38px; text-align: right; }
  .holder-name { font-size: 19px; font-weight: 400; line-height: 1; }
  .holder-name strong { font-weight: 600; }
  .holder-title { font-size: 6.8px; font-weight: 300; margin-top: 3px; }

  .contact {
    position: absolute; left: 44px; top: 161px;
    font-size: 7.6px; line-height: 11px; font-weight: 300; color: var(--ink);
  }
  .contact-line { display: flex; align-items: center; gap: 4px; }
  .contact-line strong { font-weight: 600; }
  .contact-icon { width: 6px; height: 6px; flex: none; }

  .back-wordmark {
    position: absolute; right: 42px; top: 162px;
    text-align: right; font-weight: 700; color: var(--gold);
  }
  .back-wordmark .brand-main { display: block; font-size: 13px; line-height: 1.05; }
  .back-wordmark .brand-sub { display: block; font-size: 5px; margin-top: 1px; }
</style>
</head>
<body>

<section class="card card-front">
  <svg class="accent-lines" viewBox="0 0 414 236" aria-hidden="true">
    <g fill="none" stroke="var(--gold-line)" stroke-width="0.7" opacity="0.7">
      <rect x="12" y="12" width="390" height="212"/>
      <path d="M12 52 L52 12 M12 72 L72 12"/>
      <path d="M402 184 L362 224 M402 164 L342 224"/>
    </g>
  </svg>
  <div class="front-wordmark">
    <span class="brand-main">Velvet &amp; Vine</span>
    <span class="brand-sub">by Mona</span>
  </div>
  <p class="front-tagline">POLISHED LOOKS &nbsp;•&nbsp; RADIANT DAYS</p>
</section>

<section class="card card-back">
  <svg class="accent-lines" viewBox="0 0 400 229" aria-hidden="true">
    <g fill="none" stroke="var(--gold-line)" stroke-width="0.6" opacity="0.55">
      <path d="M400 100 L271 229 M400 120 L291 229"/>
    </g>
  </svg>
  <div class="services">
    <p>Pressicion cuts</p>
    <p>Blonding, Fades</p>
    <p>Perms, Waxing &amp; more</p>
  </div>
  <p class="script-slogan">polished looks . radiant days</p>

  <div class="holder">
    <p class="holder-name"><strong>Mona</strong> Castell</p>
    <p class="holder-title">Managing Director</p>
  </div>

  <div class="contact">
    <p class="contact-line">4182 Carrow Ln. Notthingham Md, 21094 Suit 204</p>
    <p class="contact-line">
      <svg class="contact-icon" viewBox="0 0 10 10" aria-hidden="true">
        <path d="M1 1.5h8v5.2H4.2L2 8.6V6.7H1z" fill="none" stroke="#2f2f2f" stroke-width="1"/>
        <path d="M2.6 3.3h4.8M2.6 5h3.4" stroke="#2f2f2f" stroke-width="0.8"/>
      </svg>
      <span><strong>410.582.3174</strong> - Text to book an appointment</span>
    </p>
    <p class="contact-line">
      <svg class="contact-icon" viewBox="0 0 10 10" aria-hidden="true">
        <circle cx="5" cy="5" r="4" fill="none" stroke="#2f2f2f" stroke-width="1.1"/>
      </svg>
      <span>Velvet_VineByMona</span>
    </p>
  </div>

  <div class="back-wordmark">
    <span class="brand-main">Velvet &amp; Vine</span>
    <span class="brand-sub">by Mona</span>
  </div>
</section>

</body>
</html>
```